NEW Modern Sleek Business Card for VR Language Startup

Our startup is using VR to lead the next wave of world language education. We need a two-sided business card that introduces the larger organization (Quorvel Language Inc) and our contact info on one side and shows the product, Lumidrasca, on the other side.

Side 1 (contact info)= Quorvel Logo and Contact info (name, title, phone, email)

Side 2 (product)= Lumidrasc logo, text, and website
Text= Culturally Immersive Language Learning Games
Website= www.lumidrasc.example

Target Market(s)

Education, Technology

Contact Information for Business Card

Contact info will be updated upon approval of the design. For now, put this as a placeholder.

Perry Hollins
Founder & CEO
phollins@mailtrove.example
(555)-014-2736

Font styles to use
Other font styles liked:
• Gibson and Century Gothic are the brand fonts

Requirements
Nice to have
• I would love to see cohesion between the design and colors of the two logos. I have attached a few business card designs that I like, so you can get a feel for my preferred style.

```html
<!DOCTYPE html>
<html lang="en">
<head>
<meta charset="utf-8">
<title>Quorvel Language Inc — Business Card</title>
<link rel="stylesheet" href="https://fonts.googleapis.com/css2?family=Questrial&family=Montserrat:wght@700;800&display=swap">
<style>
  :root {
    --page: #ffffff;
    --card: #060709;
    --ink: #ffffff;
    --circuit-dark: #2e2e2e;
    --circuit-light: #5a5a5a;
    --product-blue: #3fa9e6;
    --brand-warm: #ee3a4f;
  }
  * { margin: 0; padding: 0; box-sizing: border-box; }
  html, body {
    width: 1200px;
    height: 1000px;
    overflow: hidden;
    background: var(--page);
  }
  .canvas {
    position: relative;
    width: 1200px;
    height: 1000px;
  }
  .card {
    position: absolute;
    top: 207px;
    width: 343px;
    height: 600px;
    border-radius: 28px;
    background: var(--card);
    overflow: hidden;
    box-shadow: 0 12px 40px rgba(0, 0, 0, 0.18);
  }
  .card--product { left: 192px; }
  .card--contact { left: 623px; }
  .card svg { display: block; }

  .ring-text {
    font-family: "Questrial", "Century Gothic", sans-serif;
    fill: var(--ink);
    font-size: 17px;
  }
  .ring-url {
    font-family: "Questrial", "Century Gothic", sans-serif;
    fill: var(--ink);
    font-size: 12.5px;
    letter-spacing: 0.5px;
  }
  .product-name {
    font-family: "Questrial", "Century Gothic", sans-serif;
    fill: var(--product-blue);
    font-size: 30px;
  }

  .brand-name {
    font-family: "Montserrat", "Century Gothic", sans-serif;
    font-weight: 800;
    fill: var(--ink);
    font-size: 30px;
    letter-spacing: 3px;
  }

  .holder {
    position: absolute;
    right: 23px;
    top: 326px;
    text-align: right;
    color: var(--ink);
  }
  .holder__name {
    font-family: "Questrial", "Century Gothic", sans-serif;
    font-size: 34px;
    line-height: 1.1;
    letter-spacing: 0.5px;
  }
  .holder__first {
    font-family: "Montserrat", "Century Gothic", sans-serif;
    font-weight: 700;
  }
  .holder__title {
    font-family: "Questrial", "Century Gothic", sans-serif;
    font-size: 18px;
    letter-spacing: 1px;
    margin-top: 4px;
  }
  .contact-list {
    position: absolute;
    left: 22px;
    top: 462px;
    list-style: none;
    color: var(--ink);
    font-family: "Questrial", "Century Gothic", sans-serif;
    font-size: 17px;
    line-height: 21.5px;
    letter-spacing: 0.6px;
  }
</style>
</head>
<body>
<main class="canvas">

  <!-- Product side -->
  <section class="card card--product" aria-label="Lumidrasc product side">
    <svg width="343" height="600" viewBox="0 0 343 600">
      <defs>
        <linearGradient id="circuitFade" x1="0" y1="0" x2="0" y2="1">
          <stop offset="0" stop-color="var(--circuit-dark)"/>
          <stop offset="0.5" stop-color="var(--circuit-light)"/>
          <stop offset="1" stop-color="var(--circuit-dark)"/>
        </linearGradient>
        <path id="taglineArc" d="M 79.4 381.5 A 128 128 0 1 1 272.6 381.5"/>
        <path id="urlArc" d="M 95 393.5 A 126 126 0 0 0 257 393.5"/>
      </defs>

      <rect class="circuit-band" x="135" y="13" width="86" height="570" rx="6"
            fill="url(#circuitFade)" opacity="0.55"
            role="img" aria-label="Vertical circuit-board trace decoration"/>

      <circle class="seal-ring" cx="176" cy="297" r="99" fill="var(--card)" stroke="var(--ink)" stroke-width="12"/>

      <text class="ring-text">
        <textPath href="#taglineArc" startOffset="50%" text-anchor="middle">CULTURALLY IMMERSIVE LANGUAGE LEARNING GAMES</textPath>
      </text>
      <circle class="ring-dot" cx="88" cy="387" r="3" fill="var(--ink)"/>
      <circle class="ring-dot" cx="264" cy="387" r="3" fill="var(--ink)"/>
      <text class="ring-url">
        <textPath href="#urlArc" startOffset="50%" text-anchor="middle">www.lumidrasc.example</textPath>
      </text>

      <circle class="product-mark" cx="176" cy="268" r="22" fill="var(--product-blue)"/>
      <text class="product-name" x="176" y="332" text-anchor="middle">Lumidrasc</text>
    </svg>
  </section>

  <!-- Contact side -->
  <section class="card card--contact" aria-label="Quorvel contact side">
    <svg width="343" height="300" viewBox="0 0 343 300" style="position:absolute;left:0;top:0;">
      <text class="brand-name" transform="translate(51 213) rotate(-90)">QUORVEL</text>
      <circle class="brand-mark" cx="220" cy="160" r="95" fill="var(--brand-warm)"/>
    </svg>

    <div class="holder">
      <p class="holder__name"><span class="holder__first">Perry</span> Hollins</p>
      <p class="holder__title">Founder &amp; CEO</p>
    </div>

    <ul class="contact-list">
      <li>123 Dummy, Lorem Ipsum</li>
      <li>phollins@mailtrove.example</li>
      <li>(555)-014-2736</li>
    </ul>
  </section>

</main>
</body>
</html>
```